Legal Journal cover - modern and sylish

We require a cover design for a new, modern and digital legal academic journal. Attached is our logo so you can get an idea of the feel. This academic journal will have several editions per year.Requirements for the cover design:-The feel of the cover is to be modern -In harmony with our logo-While staying uniform and set in its design,
Updates

Colors
ec1f27

Requirements
Must have
• 1) Colour. Each edition will use different colours. (So we will need the source files to be able to continue to do this)
• 2) An image section. We would like to be able to put in different image or photo with each edition. So we need to have a section, most likely in the shape of a strip, that can include a different image or photo each edition. This part is where we can put a different image in for each edition. So this section would need to be able to accommodate different types of images. It could be a single square. Or it could be a line (a strip) that an image or images.
• 3) A title for the edition and volume and number. Like this:
• Volume 34, No 2 (2016): Contemporary Issues in Criminal Law
• I have attached a range of journals I found online to serve as inspiration.

```html
<!DOCTYPE html>
<html lang="en">
<head>
<meta charset="utf-8">
<title>Journal Cover – Contemporary Issues in Criminal Law</title>
<link href="https://fonts.googleapis.com/css2?family=Roboto+Condensed:ital,wght@1,700&family=Arimo:wght@700&display=swap" rel="stylesheet">
<style>
  :root {
    --accent: #ec1f27;
    --accent-deep: #b5121a;
    --ink: #6a6a6a;
    --paper-top: #d9d9d9;
    --paper-bottom: #fafafa;
    --stage: #ffffff;
    --white: #ffffff;
  }
  html, body {
    margin: 0;
    padding: 0;
    width: 1200px;
    height: 1200px;
    overflow: hidden;
    background: var(--stage);
  }
  .stage {
    position: relative;
    width: 1200px;
    height: 1200px;
  }
  .cover {
    position: absolute;
    left: 210px;
    top: 49px;
    width: 958px;
    height: 1354px;
    transform: scale(0.814);
    transform-origin: 0 0;
    background: linear-gradient(180deg, var(--paper-top) 0%, #e9e9e9 55%, var(--paper-bottom) 100%);
    overflow: hidden;
  }
  .cover-art {
    position: absolute;
    inset: 0;
    width: 958px;
    height: 1354px;
  }
  .publisher {
    position: absolute;
    left: 90px;
    top: 770px;
    display: flex;
    align-items: center;
    gap: 14px;
  }
  .publisher-dot {
    width: 44px;
    height: 44px;
    border-radius: 50%;
    background: var(--accent);
  }
  .publisher-name {
    font-family: "Arimo", Arial, sans-serif;
    font-weight: 700;
    font-size: 24px;
    line-height: 1;
    letter-spacing: 1px;
    color: var(--ink);
    text-transform: uppercase;
  }
  .edition-title {
    position: absolute;
    left: 95px;
    top: 905px;
    margin: 0;
    font-family: "Roboto Condensed", "Arial Narrow", sans-serif;
    font-style: italic;
    font-weight: 700;
    font-size: 58px;
    line-height: 68px;
    color: var(--ink);
    text-transform: uppercase;
  }
  .issue-band {
    position: absolute;
    left: 0;
    right: 0;
    bottom: 0;
    height: 107px;
    background: linear-gradient(180deg, var(--accent) 0%, var(--accent-deep) 50%, var(--accent) 100%);
  }
  .issue-number {
    position: absolute;
    right: 58px;
    top: 28px;
    font-family: "Arimo", Arial, sans-serif;
    font-weight: 700;
    font-size: 30px;
    color: var(--white);
  }
</style>
</head>
<body>
<div class="stage">
  <div class="cover">
    <svg class="cover-art" viewBox="0 0 958 1354" xmlns="http://www.w3.org/2000/svg">
      <defs>
        <linearGradient id="photoTone" x1="0" y1="0" x2="1" y2="1">
          <stop offset="0" stop-color="#9a9a9a"/>
          <stop offset="0.45" stop-color="#3c3c3c"/>
          <stop offset="1" stop-color="#1e1e1e"/>
        </linearGradient>
      </defs>
      <path role="img" aria-label="Edition photo: handcuffs resting on a stack of law books beside a judge's gavel"
            fill="url(#photoTone)"
            d="M0,0 L470,0 C700,70 890,240 958,420 L958,860 C720,820 520,760 330,670 C170,590 50,470 0,300 Z"/>
      <path fill="var(--accent)" d="M470,0 L560,0 C760,80 920,260 958,470 L958,700 C930,420 760,170 470,0 Z"/>
      <path fill="var(--accent)" d="M230,25 C400,60 560,120 650,180 C520,130 380,80 230,25 Z"/>
      <path fill="var(--accent)" d="M0,300 C40,470 170,600 330,675 C520,765 720,810 920,830 C700,830 480,790 300,700 C130,610 30,480 0,320 Z"/>
      <path fill="var(--accent)" d="M480,700 C620,760 800,790 910,825 C780,815 600,780 480,700 Z"/>
      <path fill="none" stroke="var(--accent)" stroke-width="7" d="M45,235 L45,42 L96,42"/>
    </svg>

    <div class="publisher">
      <span class="publisher-dot"></span>
      <span class="publisher-name">Lexbridge Review</span>
    </div>

    <h1 class="edition-title">Contemporary<br>Issues in<br>Criminal Law</h1>

    <div class="issue-band">
      <span class="issue-number">Volume 34, No. 2, (2016)</span>
    </div>
  </div>
</div>
</body>
</html>
```